Business Card Design

I need a business card designed for my business.

The company name is Miles Renford Collective

It has four brands underneath it. They are:
- MR Occasions
- MR Athletic Journeys
- MRC Stewardship
- Dove Draftworks

I have attached all logo items, as well as our last business card.

I look forward to seeing your designs.

Industry/Entity Type

Business

Colors
eb1f27
0355a3

Requirements
Must have
• Our contact details as per the front page of our previous business card.

```html
<!DOCTYPE html>
<html lang="en">
<head>
<meta charset="utf-8">
<title>Miles Renford Collective – Business Card</title>
<link href="https://fonts.googleapis.com/css2?family=Arimo:wght@400;700&family=Tinos:wght@400;700&display=swap" rel="stylesheet">
<style>
  :root {
    --brand-red: #eb1f27;
    --brand-blue: #0355a3;
    --ink-blue: #1d4f9c;
    --paper: #ffffff;
    --backdrop: #848689;
    --soft-blue: #d6e5f6;
    --soft-peach: #f8dccb;
  }
  html, body {
    margin: 0;
    padding: 0;
    width: 1200px;
    height: 1000px;
    overflow: hidden;
    background: var(--backdrop);
  }
  .canvas {
    position: relative;
    width: 1200px;
    height: 1000px;
  }
  .card {
    position: absolute;
    width: 643px;
    height: 397px;
    background: var(--paper);
    overflow: hidden;
  }
  .card-front { left: 57px; top: 49px; }
  .card-back { left: 449px; top: 529px; }

  /* Front */
  .front-art { position: absolute; inset: 0; }
  .brand-block {
    position: absolute;
    left: 44px;
    top: 88px;
    display: flex;
    align-items: center;
    gap: 18px;
  }
  .brand-dot {
    width: 44px;
    height: 44px;
    border-radius: 50%;
    background: var(--brand-blue);
  }
  .brand-name {
    font-family: "Arimo", sans-serif;
    font-weight: 700;
    font-size: 42px;
    letter-spacing: -0.5px;
    color: var(--brand-blue);
  }
  .contact {
    position: absolute;
    display: flex;
    align-items: center;
    gap: 14px;
    font-family: "Arimo", sans-serif;
    font-size: 15.5px;
    letter-spacing: 1.2px;
    line-height: 19px;
    color: var(--ink-blue);
  }
  .contact svg { flex: none; }
  .contact-person { left: 37px; top: 226px; }
  .contact-phone { left: 37px; top: 273px; }
  .contact-web { left: 283px; top: 226px; }
  .contact-post { left: 283px; top: 273px; }

  /* Back */
  .back-top { position: absolute; left: 0; top: 0; width: 100%; height: 154px; background: var(--brand-red); }
  .back-stripe-red { position: absolute; left: 0; top: 261px; width: 100%; height: 76px; background: var(--brand-red); }
  .back-stripe-blue { position: absolute; left: 0; top: 337px; width: 100%; height: 60px; background: var(--brand-blue); }
  .tagline {
    position: absolute;
    left: 42px;
    top: 174px;
    margin: 0;
    font-family: "Tinos", serif;
    font-weight: 700;
    color: var(--ink-blue);
  }
  .tagline-lead { display: block; font-size: 37px; line-height: 42px; letter-spacing: 3.5px; }
  .tagline-tail { display: block; font-size: 27px; line-height: 32px; padding-left: 191px; letter-spacing: 3.2px; }
  .brand-strip {
    position: absolute;
    left: 28px;
    top: 278px;
    width: 586px;
    height: 94px;
    background: var(--paper);
    border-radius: 10px;
    display: flex;
    align-items: center;
    justify-content: space-around;
    padding: 0 6px;
    box-sizing: border-box;
  }
  .sub-brand {
    font-family: "Arimo", sans-serif;
    font-weight: 700;
    font-size: 15px;
    white-space: nowrap;
  }
  .sub-brand.red { color: var(--brand-red); }
  .sub-brand.blue { color: var(--brand-blue); }
</style>
</head>
<body>
<main class="canvas">

  <section class="card card-front" aria-label="Business card front">
    <svg class="front-art" width="643" height="397" viewBox="0 0 643 397">
      <defs>
        <linearGradient id="art-wash" x1="0" y1="0" x2="1" y2="0">
          <stop offset="0" stop-color="var(--soft-blue)" stop-opacity="0"/>
          <stop offset="0.35" stop-color="var(--soft-blue)" stop-opacity="0.7"/>
          <stop offset="1" stop-color="var(--soft-peach)" stop-opacity="0.8"/>
        </linearGradient>
      </defs>
      <rect x="420" y="205" width="223" height="135" fill="url(#art-wash)" role="img" aria-label="Background illustration: globe with an outstretched arm"/>
      <path d="M0 338 Q330 368 643 272 L643 397 L0 397 Z" fill="var(--brand-red)"/>
      <path d="M0 350 Q330 372 643 290 L643 397 L0 397 Z" fill="var(--brand-blue)"/>
    </svg>

    <div class="brand-block">
      <span class="brand-dot"></span>
      <span class="brand-name">Miles Renford Collective</span>
    </div>

    <div class="contact contact-person">
      <svg width="34" height="34" viewBox="0 0 26 26" aria-hidden="true">
        <circle cx="13" cy="13" r="12" fill="none" stroke="var(--brand-blue)" stroke-width="1.5"/>
        <circle cx="13" cy="9" r="3.5" fill="var(--brand-red)"/>
        <path d="M6.5 20 Q13 11 19.5 20 Z" fill="var(--brand-red)"/>
      </svg>
      <div>Miles Renford<br>Principal</div>
    </div>

    <div class="contact contact-phone">
      <svg width="34" height="34" viewBox="0 0 26 26" aria-hidden="true">
        <circle cx="13" cy="13" r="12" fill="none" stroke="var(--brand-blue)" stroke-width="1.5"/>
        <path d="M8 7 L10.5 6.5 L12 10 L10.5 11.5 Q12 15 15 16 L16.5 14.5 L20 16 L19.5 18.5 Q15 20 11 16 Q7 12 8 7 Z" fill="var(--brand-red)"/>
      </svg>
      <div>+61 2 5550 1482<br>+61 400 555 318</div>
    </div>

    <div class="contact contact-web">
      <svg width="34" height="34" viewBox="0 0 26 26" aria-hidden="true">
        <circle cx="13" cy="13" r="12" fill="none" stroke="var(--brand-blue)" stroke-width="1.5"/>
        <circle cx="13" cy="13" r="7" fill="none" stroke="var(--brand-red)" stroke-width="1.6"/>
        <ellipse cx="13" cy="13" rx="3" ry="7" fill="none" stroke="var(--brand-red)" stroke-width="1.3"/>
        <line x1="6" y1="13" x2="20" y2="13" stroke="var(--brand-red)" stroke-width="1.3"/>
      </svg>
      <div>Miles@MilesRenford.com.au<br>www.MilesRenford.com.au</div>
    </div>

    <div class="contact contact-post">
      <svg width="34" height="34" viewBox="0 0 26 26" aria-hidden="true">
        <circle cx="13" cy="13" r="12" fill="none" stroke="var(--brand-blue)" stroke-width="1.5"/>
        <path d="M13 21 Q7 14 7 11 A6 6 0 0 1 19 11 Q19 14 13 21 Z" fill="var(--brand-red)"/>
        <circle cx="13" cy="11" r="2.3" fill="var(--paper)"/>
      </svg>
      <div>PO Box 418, Belconnen<br>ACT 2617 Australia.</div>
    </div>
  </section>

  <section class="card card-back" aria-label="Business card back">
    <div class="back-top"></div>
    <h2 class="tagline">
      <span class="tagline-lead">Event, travel and</span>
      <span class="tagline-tail">talent management</span>
    </h2>
    <div class="back-stripe-red"></div>
    <div class="back-stripe-blue"></div>
    <div class="brand-strip">
      <span class="sub-brand red">MR Athletic Journeys</span>
      <span class="sub-brand blue">MR Occasions</span>
      <span class="sub-brand blue">MRC Stewardship</span>
      <span class="sub-brand red">Dove Draftworks</span>
    </div>
  </section>

</main>
</body>
</html>
```